New Church Home Page and Content Page Design

Our church, Harbor Light Baptist Church www.hlbtvkx.org, needs an update for our online presence. The homepage design should provide the following 4 pieces of information above the fold:
1. Church location - 47 Pinecrest Hollow Lane in Chappaqua, NY, USA.
2. Service times and types Sunday school, children's church, etc..
3. A space for some text describing us and our beliefs - a Bible believing independent Baptist church.
4. photos of our members to give visitors an impression of what kind of people attend our church - a friendly group of culturally diverse people who love Jesus.

In addition to the homepage we need a design for internal pages of general content. The content page design should provide a lot of room for content and prominent navigation area. We will use this design to host pages with content such as:
A full description of our beliefs
A photo gallery
An event calendar
Embedded audio and video of past sermons
A member directory
etc.
Updates

Thanks everyone for your submissions. I'll be meeting with our Pastor tomorrow. I am working as fast as I can to review all the designs and come up with a short list for him. A decision should be close behind.

Target Market(s)

Local people looking for a church.

Industry/Entity Type

Church

Requirements
Must have
• 1. Place to show church location - Westchester county, New York State, USA.
2. Place to list service times and types.
3. A space for some text describing us and our beliefs.
4. A place to display photos of our members (see also the nice to have section)
Nice to have
• Would be great if the member photos (#4 in must have section) displayed the images in some innovative way. I rather not have an ordinary carousel of images.

```html
<!DOCTYPE html>
<html lang="en">
<head>
<meta charset="utf-8">
<title>Harbor Light Baptist Church</title>
<link href="https://fonts.googleapis.com/css2?family=Fira+Sans:wght@400;500;600&family=Open+Sans:wght@400;600;700&display=swap" rel="stylesheet">
<style>
:root{
  --navy:#1d3a5c;
  --navy-dark:#142b47;
  --nav-top:#2b5078;
  --nav-bottom:#18375a;
  --text:#555;
  --muted:#888;
  --rule:#dcdcdc;
  --yellow:#f5c56e;
  --teal:#62c8c4;
  --green:#80c878;
  --coral:#f98670;
  --footer:#2e2e2e;
}
*{box-sizing:border-box;margin:0;padding:0}
html,body{width:676px;height:1200px;overflow:hidden;background:#fff}
body{position:relative;font-family:"Open Sans",Arial,sans-serif;color:var(--text)}
.abs{position:absolute}

/* header */
.brand{left:46px;top:30px;display:flex;align-items:center;gap:8px}
.brand-mark{width:38px;height:38px;background:var(--navy)}
.brand-name{font-family:"Fira Sans",sans-serif;font-weight:600;font-size:14px;line-height:15px;color:var(--navy);width:110px}
.address{right:48px;top:22px;font-size:10px;color:var(--navy);display:flex;align-items:center;gap:7px}
.search{right:48px;top:56px;width:148px;height:20px;border:1px solid #ccc;font-size:9px;color:#999;padding:4px 6px;display:flex;justify-content:space-between;align-items:center}

/* nav */
.nav{left:0;top:95px;width:676px;height:33px;background:linear-gradient(var(--nav-top),var(--nav-bottom))}
.nav ul{list-style:none;display:flex;margin-left:47px;height:100%}
.nav li{font-size:10px;font-weight:700;color:#fff;display:flex;align-items:center;justify-content:center;border-right:1px solid rgba(255,255,255,.12);height:100%}
.nav li.active{background:#3d6690}

/* hero */
.hero{left:0;top:128px;width:676px;height:270px;background:radial-gradient(circle at 62% 25%,#fffbe8 0,#e7eef5 18%,#9db8d2 55%,#6c8fb5 100%)}
.hero-bar{left:0;top:397px;width:676px;height:3px;background:var(--navy-dark)}
.arrow-btn{top:254px;width:36px;height:36px;border-radius:50%;background:rgba(60,60,60,.45);display:flex;align-items:center;justify-content:center}
.caption{left:74px;top:322px;height:40px;padding:0 16px;background:rgba(40,40,40,.65);color:#fff;font-family:"Fira Sans",sans-serif;font-size:17px;display:flex;align-items:center;letter-spacing:.3px}

/* headings */
.h-section{font-family:"Fira Sans",sans-serif;color:var(--navy);font-size:15px;font-weight:400}
.ruled{left:46px;width:582px;display:flex;align-items:center;gap:22px}
.ruled::before,.ruled::after{content:"";flex:1;height:3px;border-top:1px solid var(--rule);border-bottom:1px solid var(--rule)}
.ruled .h-section{font-size:13px;font-weight:500}
.p{font-size:8.6px;line-height:15.5px;color:var(--text)}

/* welcome */
.welcome-img{left:46px;top:461px;width:124px;height:112px;background:radial-gradient(circle at 50% 30%,#f3dca0,#b88a4a 55%,#3c2a18)}
.services .item{font-size:9px;color:var(--text);margin-top:9px;padding-bottom:8px}
.services .item small{display:block;font-size:8px;color:var(--muted);margin:4px 0 0 9px}
.services .item+.item{border-top:1px solid var(--rule);padding-top:9px}

/* beliefs */
.beliefs-img{left:47px;top:660px;width:258px;height:133px;background:linear-gradient(90deg,#6b5a2e,#e9e4d4 25%,#c9a893 55%,#9fb4c9)}

/* members */
.pager{right:48px;top:836px;display:flex;gap:4px}
.pager span{width:15px;height:15px;border-radius:50%;background:#ccc}
.grid{left:47px;top:882px;width:582px;height:222px;display:grid;grid-template-columns:repeat(4,1fr);grid-template-rows:repeat(2,1fr);gap:1px}
.tile{display:flex;flex-direction:column;align-items:center;justify-content:center;color:#fff;font-family:"Fira Sans",sans-serif;position:relative}
.tile .name{font-size:16px;font-weight:500;padding-bottom:8px;border-bottom:1px solid rgba(255,255,255,.6);width:80%;text-align:center}
.tile .place{font-size:14px;margin-top:8px}
.tile.pointer::before{content:"";position:absolute;left:-6px;top:50px;border:6px solid transparent;border-left:0;border-right-color:var(--yellow)}
.yellow{background:var(--yellow)}.teal{background:var(--teal)}.green{background:var(--green)}.coral{background:var(--coral)}
.photo-a{background:linear-gradient(160deg,#f2f2f2,#c9c9c9 60%,#3a3a3a)}
.photo-b{background:linear-gradient(160deg,#eaf6fa,#cfe7ef 60%,#8fb7c7)}
.photo-c{background:radial-gradient(circle at 70% 20%,#fff3c8,#c98a42 50%,#4b2b14)}
.photo-d{background:linear-gradient(160deg,#f0f0f0,#d6d6d6 60%,#3f4a5a)}

/* footer */
.footer{left:0;top:1139px;width:676px;height:61px;background:var(--footer)}
.footer-links{left:46px;top:1158px;font-family:Arial,sans-serif;font-size:8.5px;color:#fff}
.copy{left:46px;top:1179px;font-family:Arial,sans-serif;font-size:8px;color:#ddd}
.social{right:48px;top:1166px;display:flex;gap:8px}
.social span{width:20px;height:20px}
</style>
</head>
<body>

<header>
  <div class="abs brand"><div class="brand-mark"></div><div class="brand-name">Harbor Light Baptist Church</div></div>
  <div class="abs address">
    <svg width="8" height="12" viewBox="0 0 8 12"><path d="M4 0a4 4 0 0 0-4 4c0 3 4 8 4 8s4-5 4-8a4 4 0 0 0-4-4z" fill="#1d3a5c"/><circle cx="4" cy="4" r="1.5" fill="#fff"/></svg>
    47 Pinecrest Hollow Lane, Chappaqua, NY, USA
  </div>
  <div class="abs search"><span>Search..</span>
    <svg width="9" height="9" viewBox="0 0 9 9"><circle cx="3.6" cy="3.6" r="2.8" fill="none" stroke="#999" stroke-width="1.2"/><path d="M5.7 5.7 8.5 8.5" stroke="#999" stroke-width="1.3"/></svg>
  </div>
</header>

<nav class="abs nav">
  <ul>
    <li class="active" style="width:64px">HOME</li>
    <li style="width:99px">CONTACT US</li>
    <li style="width:85px">CALENDAR</li>
    <li style="width:90px">MINISTRIES</li>
    <li style="width:106px">SERVICE TIMES</li>
    <li style="width:136px;border-right:0">SERMONS AND MEDIA</li>
  </ul>
</nav>

<section>
  <div class="abs hero" role="img" aria-label="Wooden cross against a bright sky with clouds and sun rays"></div>
  <div class="abs hero-bar"></div>
  <div class="abs arrow-btn" style="left:46px"><svg width="8" height="14"><path d="M7 1 1 7l6 6" fill="none" stroke="#fff" stroke-width="1.2"/></svg></div>
  <div class="abs arrow-btn" style="right:46px"><svg width="8" height="14"><path d="M1 1l6 6-6 6" fill="none" stroke="#fff" stroke-width="1.2"/></svg></div>
  <div class="abs caption">DUS AUTM VEUM IRIRE DOOR DUIS MOLLIS</div>
</section>

<section>
  <h2 class="abs h-section" style="left:46px;top:428px">WELCOME TO HARBOR LIGHT BAPTIST CHURCH</h2>
  <div class="abs welcome-img" role="img" aria-label="Silhouettes of a group gathered before a cross in golden light"></div>
  <p class="abs p" style="left:191px;top:457px;width:236px">Lorem ipsum dolor sit amet, consectetur adipiisicing elit. Suscipit illo voluptas aperiam repudiandae impedit quidem. Lorem ipsum dolor sit amet, cctetuir adipisicing elit. Suscipit illo voluptas aperiam repudiandae impeidit quidem. Lorem ipsum dolor sit amet, consectetur adipisicing elit. Suscipit illo voluptas aperiam repudiandae impedit quidem. Lorem ipsum dolor sit amet, consectetur adipisicing elit. Suscnipt illo voluptas aperiam repudiandae impedit quidem.</p>

  <div class="abs services" style="left:471px;top:430px;width:157px">
    <h2 class="h-section">OUR SERVICES</h2>
    <p class="p" style="font-size:8px;line-height:14px;margin-top:6px">Lorem ipsum dolor sit amet consecteuer adipiscing elit Nam cursus Morbi ut mi.</p>
    <div class="item">&#9656; Sunday School @ California<small>Tuesday 9.00 AM</small></div>
    <div class="item">&#9656; Children's Church @ Texas<small>Tuesday 9.00 AM</small></div>
  </div>
</section>

<section>
  <div class="abs ruled" style="top:615px"><h2 class="h-section">OUR BELIEFS</h2></div>
  <div class="abs beliefs-img" role="img" aria-label="Woman with head bowed in prayer"></div>
  <h3 class="abs" style="left:341px;top:654px;font-size:13px;font-weight:400;color:#444">A Bible believing independent Baptist church</h3>
  <p class="abs p" style="left:341px;top:676px;width:290px;font-size:8.2px;line-height:14px">Typi non habent claritatem insitam; est usus legentis in iis qui facit eorum claritatem. Investigationes demonstraverunt lectores legere me lius quod ii legunt saepius.</p>
  <p class="abs p" style="left:341px;top:723px;width:290px;font-size:8.2px;line-height:14px">Claritas est etiam processus dynamicus, qui sequitur mutationem consuetudium lectorum. Mirum est notare quam littera gothica, quam nunc putamus parum claram, anteposuerit litterarum formas humanitatis per seacula quarta decima et quinta decima. Eodem modo typi, qui nunc nobis videntur parum clari, fiant sollemnes in futurum.</p>
</section>

<section>
  <div class="abs ruled" style="top:835px;width:540px"><h2 class="h-section">OUR MEMEBRS</h2></div>
  <div class="abs pager"><span></span><span></span></div>
  <div class="abs grid">
    <div class="photo-a" role="img" aria-label="Portrait of a smiling man in a dark jacket"></div>
    <div class="tile yellow pointer"><div class="name">Mr. Ben Orly</div><div class="place">France</div></div>
    <div class="photo-b" role="img" aria-label="Portrait of a smiling woman with short hair"></div>
    <div class="tile teal"><div class="name">Mr. Sam Vell</div><div class="place">France</div></div>
    <div class="tile green"><div class="name">Ms. Ada Vell</div><div class="place">Texas</div></div>
    <div class="photo-c" role="img" aria-label="Woman praying in warm light"></div>
    <div class="tile coral"><div class="name">Mr. Sam Vell</div><div class="place">California</div></div>
    <div class="photo-d" role="img" aria-label="Portrait of a smiling young man"></div>
  </div>
</section>

<footer>
  <div class="abs footer"></div>
  <div class="abs footer-links">Home | Contact Us | Calendar | Ministries | Service Times | Sermons and Media</div>
  <div class="abs copy">Copyright &copy; 2013. All Rights Reserved.</div>
  <div class="abs social">
    <span style="background:#3b5998"></span>
    <span style="background:#2fa3d8"></span>
    <span style="background:#f26b1d"></span>
    <span style="background:#d9302a"></span>
  </div>
</footer>

</body>
</html>
```